Harwick Legal

To update and modernize current business card appearance. Marta's business is based in Melbourne with 4 other lawyers in the firm. Marta travels to the Pilbara in Western Australia approximately 1 week a month as part of the firms legal work. She consults with clients in Newman, Tom Price and Port Hedland. The lawyers work mostly from a home office, apart from court appearances. They have a virtual office in Melbourne city, and use facilities in 3 or 4 other locations around Melbourne. It is important the client's think this is a conventional law firm with a permanent office. Our business structure is a difficult concept for them to grasp. The business has been operational for 3 years, growing from 1 lawyer to 4 lawyers during that time. Our website is www.Harwicklegal.example.au and is currently being upgraded as we are not happy with its content. The logo is currently orange and dark grey but the orange is a difficult colour to reproduce and often turns out "poo" brown when documents are printed. We need clients to know we are user friendly and caring - and not head up our rears ends as some lawyers appear to be.
Updates

Thank you for the feedback so far. 1. Some of the designs have too much black (We prefer darker grey & not too much.) 2. Happy for designers to play around with different colours & logo design. What we're after is a modern look and business card that people say "wow" when they pick it up.

Industry/Entity Type

Business

```html
<!DOCTYPE html>
<html lang="en">
<head>
<meta charset="utf-8">
<title>Harwick Legal – Business Card</title>
<link href="https://fonts.googleapis.com/css2?family=Montserrat:wght@300;400;600;700&display=swap" rel="stylesheet">
<style>
  :root {
    --page: #f4f4f4;
    --card: #555456;
    --ink: #ffffff;
    --ink-soft: #d9d9d9;
    --rule: #9a9a9a;
    --badge: #ffffff;
    --badge-ring: #8a8a8a;
    --badge-ink: #555456;
    --accent: #e2513a;
  }
  * { box-sizing: border-box; margin: 0; padding: 0; }
  html, body { width: 1200px; height: 1000px; overflow: hidden; }
  body {
    background: var(--page);
    font-family: "Montserrat", sans-serif;
    color: var(--ink);
    display: flex;
    align-items: center;
    justify-content: center;
    gap: 40px;
  }
  .card {
    width: 530px;
    height: 322px;
    background: var(--card);
    border-radius: 4px;
    box-shadow: 0 10px 30px rgba(0,0,0,0.18);
    position: relative;
    padding: 34px 40px;
  }

  /* Brand badge */
  .badge {
    width: 74px; height: 74px;
    border-radius: 50%;
    background: var(--badge);
    border: 4px solid var(--badge-ring);
    display: flex; align-items: center; justify-content: center;
    text-align: center;
    font-size: 10px; font-weight: 600; line-height: 1.15;
    color: var(--badge-ink);
  }
  .badge--small {
    width: 20px; height: 20px; border-width: 2px;
    font-size: 0;
  }

  /* Front */
  .front .badge { margin-left: 6px; }
  .front__rule {
    width: 110px; height: 2px; background: var(--rule);
    margin: 12px 0 10px 0;
  }
  .contact { font-size: 13.5px; font-weight: 300; line-height: 1.45; letter-spacing: 0.2px; }
  .contact__name { font-weight: 700; font-size: 14px; letter-spacing: 0.4px; text-transform: uppercase; }
  .contact__line { display: flex; align-items: center; gap: 6px; }
  .contact__line svg { width: 13px; height: 13px; }
  .tagline {
    position: absolute; right: 40px; bottom: 36px;
    font-size: 15px; font-weight: 600; letter-spacing: 0.2px;
  }

  /* Back */
  .back { display: flex; flex-direction: column; justify-content: center; padding-left: 58px; }
  .practice__title {
    font-size: 15px; font-weight: 700; letter-spacing: 0.8px;
    text-transform: uppercase;
    padding-bottom: 5px;
    border-bottom: 2px solid var(--rule);
    align-self: flex-start;
    margin-left: 50px;
  }
  .practice__list {
    list-style: none; margin: 8px 0 6px 90px;
    font-size: 14px; font-weight: 300; line-height: 1.35; color: var(--ink-soft);
  }
  .back .badge--small { margin: 4px 0 6px 150px; }
  .motto {
    font-size: 21px; font-weight: 700; letter-spacing: 0.6px; text-transform: uppercase;
  }
  .inquiries { font-size: 10.5px; font-weight: 300; margin: 4px 0 0 34px; }
  .inquiries strong { font-weight: 600; }
</style>
</head>
<body>

  <section class="card front" aria-label="Business card front">
    <div class="badge" aria-label="Harwick Legal">Harwick<br>Legal</div>
    <div class="front__rule"></div>
    <div class="contact">
      <p class="contact__name">J. Marta Ellison</p>
      <p>LLB ( Hons ) - Accredited Mediator</p>
      <p>Principal Solicitor</p>
      <p>1300 Harwick ( 427 942 )</p>
      <p class="contact__line">
        <svg viewBox="0 0 16 16" aria-hidden="true"><circle cx="8" cy="8" r="7" fill="none" stroke="#fff" stroke-width="1.2"/><path d="M5.6 4.4l1.3 1.7-.8 1c.5 1 1.3 1.8 2.3 2.3l1-.8 1.7 1.3-.8 1.4C8 11.2 4.8 8 4.2 5.2z" fill="#fff"/></svg>
        0491 570 118
      </p>
      <p>marta.ellison@harwicklegal.example.au</p>
    </div>
    <p class="tagline">Serving the People of the Pilbara</p>
  </section>

  <section class="card back" aria-label="Business card back">
    <h2 class="practice__title">Areas of Practice :</h2>
    <ul class="practice__list">
      <li>Family Law</li>
      <li>Collaborative Practice</li>
      <li>Mediation &amp; Negotiation</li>
      <li>Intervention Orders</li>
      <li>Criminal Law</li>
    </ul>
    <div class="badge badge--small" aria-label="Harwick Legal"></div>
    <p class="motto">Experience.Support. Solutions</p>
    <p class="inquiries"><strong>Inquiries :</strong> info@harwicklegal.example.au</p>
  </section>

</body>
</html>
```